Exciting, Bold and Modern Landscaping & Turf care company business card

Hello, I own a lawn and landscaping company in Virginia, USA. We would like to design a bold, dynamic, modern business card that really makes us stand out. I tire of all green business cards with crappy, cartoonish clipart grass on them. It needs to be two sided, on one side i need to highlight our turf care division called "Promised Brighter Meadow" We maintain grass, fertilize it, weed control, etc.. We have a green thumbed gopher as our logo that i will attach. I am looking for something, clean and neat but out of the box in style. Im open to all ideas, and would like different options for them. On the other side, i want to highlight our landscaping division "Quiet Harbor Landscaping" In this division we design and install landscapes. Feel free to visit our website for more info or email me with ANY questions. Our busines cards in the past have highlighted our different services, but i don't want to this time. By the time I hand out a business card we are usually already estimating a project and they know what services we offer. I do want them to look at my card and say "wow thats pretty cool" and for them to think "These guys are something different, not just your standard dirt diggers" The logo doesnt have to be on both sides, but it needs to be on the turf care side. Our phone number and website should also be on at least on side, but need not be on both. The phone number is (555)618-4072 as well as the web address as www.MossbrookYardWorks.example. I like for the web address to have caps like that becasue it makes the long address much easier to read. I would like it in full color, printing costs are not my major concern. I also love rounded corners or interesting die cut designs as well, so feel free to wow me. Whether it be a clean white background with a bold photo to an all black card with a gray logo except for his green thumb with silver foil lettering to anything in between, lets go for it. That bieng said i dont want anything cartoonish, we are still a professional service and i want that to come through. THANKS!
Updates
Project Deadline Extended
Reason: changed project to a committed payment. I would like designers to re-evaluate their interest now and give them extra time to submit designs. Thank you.
we have changed our status to a commited payment to entice more submissions. thank you all for your hard work!
Industry/Entity Type
Professional Service
Look and feel
Each slider illustrates characteristics of the customer's brand and the style your logo design should communicate.

```html
<!DOCTYPE html>
<html lang="en">
<head>
<meta charset="utf-8">
<title>Quiet Harbor Landscaping – Business Card</title>
<link rel="stylesheet" href="https://fonts.googleapis.com/css2?family=Oswald:wght@400;500;600&display=swap">
<style>
  :root {
    --page: #dfe9f2;
    --card-black: #1d1c1c;
    --band-black: #252322;
    --leaf: #8fd13a;
    --leaf-soft: #7fc23a;
    --gold: #f2e21c;
    --turf: #3aa83a;
    --turf-dark: #23832b;
    --lawn-deep: #1f5a22;
    --garden-deep: #2f5a22;
    --garden-mid: #5f8f34;
    --garden-light: #a9c45a;
    --gravel: #b9b9bd;
    --sky: #cfe4f5;
    --lawn: #5f9a3a;
  }
  * { box-sizing: border-box; margin: 0; padding: 0; }
  html, body { width: 1200px; height: 646px; overflow: hidden; }
  body {
    background: var(--page);
    font-family: "Oswald", "Arial Narrow", sans-serif;
    display: flex;
    align-items: center;
    justify-content: center;
    gap: 40px;
  }
  .card {
    position: relative;
    width: 540px;
    height: 309px;
    border-radius: 10px;
    overflow: hidden;
    box-shadow: 0 6px 18px rgba(30, 50, 70, 0.25);
  }

  /* Landscaping side */
  .garden-photo {
    position: absolute; inset: 0;
    background: linear-gradient(180deg, var(--garden-deep) 0%, var(--garden-mid) 45%, var(--garden-light) 62%, var(--gravel) 100%);
  }
  .title-band {
    position: absolute;
    left: -40px; top: 92px;
    width: 640px; height: 92px;
    background: var(--band-black);
    transform: rotate(-9deg);
    display: flex; flex-direction: column; align-items: center; justify-content: center;
  }
  .title-band::before, .title-band::after {
    content: ""; position: absolute; left: 40px; right: 40px; height: 2px; background: var(--gold);
  }
  .title-band::before { top: 8px; }
  .title-band::after { bottom: 8px; }
  .company-name {
    font-weight: 600; font-size: 36px; letter-spacing: 1px; text-transform: uppercase;
    color: var(--leaf); line-height: 1.1;
  }
  .company-name .accent { color: var(--gold); }
  .company-tagline {
    font-weight: 400; font-size: 14px; letter-spacing: 2px; text-transform: uppercase;
    color: var(--leaf-soft);
  }

  /* Turf care side */
  .card--turf { background: var(--card-black); }
  .turf-photo {
    position: absolute; left: 0; bottom: 0;
    width: 250px; height: 240px;
    background: linear-gradient(180deg, var(--sky) 0%, var(--sky) 28%, var(--lawn) 60%, var(--lawn-deep) 100%);
  }
  .turf-photo .torn-edge { position: absolute; right: -1px; top: 0; height: 100%; width: 20px; }
  .brand-mark {
    position: absolute; left: 22px; bottom: 22px;
    display: flex; align-items: center; gap: 10px;
  }
  .brand-mark .dot {
    width: 18px; height: 18px; border-radius: 50%; background: var(--leaf);
  }
  .brand-mark .brand-name {
    font-weight: 500; font-size: 24px; text-transform: uppercase; letter-spacing: 0.5px;
    color: var(--gold); line-height: 1;
  }
  .web {
    position: absolute; right: 24px; top: 20px;
    font-size: 14px; color: var(--leaf); letter-spacing: 0.3px;
  }
  .turf-band {
    position: absolute; right: 0; top: 56px;
    width: 330px; height: 44px;
    background: linear-gradient(90deg, var(--turf-dark), var(--turf));
    display: flex; align-items: center; padding-left: 18px;
  }
  .turf-band span {
    font-weight: 600; font-size: 22px; text-transform: uppercase; color: var(--gold); letter-spacing: 0.5px;
  }
  .contact {
    position: absolute; right: 24px; top: 128px;
    text-align: right; color: var(--leaf);
  }
  .contact .person { font-size: 30px; font-weight: 500; text-transform: uppercase; line-height: 1.2; }
  .contact .phone { font-size: 20px; color: var(--gold); margin-top: 6px; }
  .contact .email { font-size: 15px; color: var(--gold); margin-top: 8px; }
</style>
</head>
<body>
  <section class="card card--landscape">
    <div class="garden-photo" role="img" aria-label="Photo of a landscaped garden with evergreen shrubs, boulders, timber step and gravel path"></div>
    <div class="title-band">
      <h1 class="company-name">Quiet Harbor <span class="accent">Landscaping</span></h1>
      <p class="company-tagline">Family owned and operated since 1995</p>
    </div>
  </section>

  <section class="card card--turf">
    <div class="turf-photo" role="img" aria-label="Photo of a mown lawn and trees under a blue sky">
      <svg class="torn-edge" viewBox="0 0 20 240" preserveAspectRatio="none" aria-hidden="true">
        <polygon points="20,0 8,20 14,45 6,70 13,100 5,130 12,160 4,190 11,215 6,240 20,240" fill="var(--card-black)"/>
      </svg>
    </div>
    <div class="brand-mark">
      <span class="dot" aria-hidden="true"></span>
      <span class="brand-name">Quiet Harbor</span>
    </div>
    <p class="web">www.MossbrookYardWorks.example</p>
    <div class="turf-band"><span>Promised Brighter Meadow</span></div>
    <div class="contact">
      <p class="person">Dale Whitcomb</p>
      <p class="phone">P: 555-618-4072</p>
      <p class="email">E: QuietHarborYards@mail.example</p>
    </div>
  </section>
</body>
</html>
```